World first health care product in tablet form to help save relationships and marriages

The product known as Zentharo is in tablet form 470mg and has 30 to a packet the packet size is approx 11cm in length x 4cm We want to use the color of the image attached for the package and cornflower blue for our name Zentharo. We also need to mention close to our name....... maintaining relationships with increased libido and desire ...... Our tablets are in a tamper-proof blister pack inserted into the package. We do not have a logo as yet, we are thinking of zen in small white letters and then THARO in large letters in cornflower blue or something a bit darker. (The O could also contain a smiley face) We are not that fussed with a logo as yet, maybe down the track if our product works and sells. As of today business in Australia has ground to a halt with this coronavirus and its as bad as you could imagine. Please help us make this new product work with a fabulous packet design.
Target Market(s)
females and males
Industry/Entity Type
Pharmaceutical
Requirements
Must have
- the colors of the images attached and cornflower blue

```html
<!DOCTYPE html>
<html lang="en">
<head>
<meta charset="utf-8">
<title>Zentharo – Packaging Fronts</title>
<link rel="stylesheet" href="https://fonts.googleapis.com/css2?family=Montserrat:wght@500;600;800&display=swap">
<style>
  :root {
    --page: #ffffff;
    --pack-sky: #9ddbf5;
    --halftone: #4cbfee;
    --halftone-soft: #7ccff2;
    --brand-blue: #0a6bb5;
    --white: #ffffff;
  }
  * { margin: 0; padding: 0; box-sizing: border-box; }
  html, body {
    width: 1200px; height: 927px; overflow: hidden;
    background: var(--page);
    font-family: "Montserrat", Arial, sans-serif;
  }
  .canvas { position: relative; width: 1200px; height: 927px; }

  .pack {
    position: absolute;
    background: var(--pack-sky);
    overflow: hidden;
  }
  .pack-tall { left: 124px; top: 153px; width: 172px; height: 473px; }
  .pack-wide { left: 421px; top: 153px; width: 473px; height: 172px; }

  .halftone { position: absolute; inset: 0; }
  .pack-tall .halftone {
    background:
      linear-gradient(to left, var(--halftone-soft) 0%, rgba(124,207,242,0) 18%),
      linear-gradient(to bottom, var(--halftone) 0%, var(--halftone-soft) 22%, var(--pack-sky) 62%, var(--pack-sky) 100%);
  }
  .pack-wide .halftone {
    background: linear-gradient(to right, var(--pack-sky) 0%, var(--pack-sky) 45%, var(--halftone-soft) 78%, var(--halftone) 100%);
  }

  .wordmark {
    position: absolute;
    display: flex; align-items: center;
    color: var(--brand-blue);
    font-weight: 800;
    letter-spacing: -0.02em;
    line-height: 1;
    white-space: nowrap;
  }
  .wordmark .dot {
    display: inline-block;
    flex: none;
    border-radius: 50%;
    background: var(--white);
  }
  .pack-tall .wordmark { left: 20px; top: 212px; font-size: 25px; gap: 5px; }
  .pack-tall .wordmark .dot { width: 13px; height: 13px; }
  .pack-wide .wordmark { left: 36px; top: 62px; font-size: 52px; gap: 9px; }
  .pack-wide .wordmark .dot { width: 24px; height: 24px; }

  .tagline {
    position: absolute;
    color: var(--brand-blue);
    font-weight: 500;
    white-space: nowrap;
  }
  .pack-tall .tagline { left: 22px; top: 270px; font-size: 10.5px; line-height: 12.5px; }
  .pack-wide .tagline { left: 37px; top: 128px; font-size: 12px; line-height: 15px; }

  .dosage {
    position: absolute;
    color: var(--white);
    font-weight: 600;
    white-space: nowrap;
  }
  .dosage span + span { margin-left: 14px; }
  .pack-tall .dosage-band {
    position: absolute; left: 0; top: 439px; width: 100%; height: 22px;
    background: var(--brand-blue);
  }
  .pack-tall .dosage { left: 32px; top: 443px; font-size: 11.5px; }
  .pack-wide .dosage { left: 314px; top: 135px; font-size: 12px; opacity: 0.95; }
</style>
</head>
<body>
<main class="canvas">

  <section class="pack pack-tall" aria-label="Zentharo pack, end panel">
    <div class="halftone" role="img" aria-label="Halftone dot pattern fading down from the top"></div>
    <div class="wordmark"><span class="dot"></span>Zentharo</div>
    <p class="tagline">Maintaining<br>relationships<br>with increased<br>libido and desire</p>
    <div class="dosage-band"></div>
    <p class="dosage"><span>470mg</span><span>30 Tablets</span></p>
  </section>

  <section class="pack pack-wide" aria-label="Zentharo pack, front panel">
    <div class="halftone" role="img" aria-label="Halftone dot pattern fading in from the right"></div>
    <div class="wordmark"><span class="dot"></span>Zentharo</div>
    <p class="tagline">Maintaining relationships<br>with increased libido and desire</p>
    <p class="dosage"><span>470mg</span><span>30 Tablets</span></p>
  </section>

</main>
</body>
</html>
```